Business Card Design for Consulting Company

I require a Business Card design for my Consulting company. <br/><br/>My company name is: Marek Olvani Consulting Inc.<br/>My website is: www.marekolvaniconsulting.example<br/><br/>My company focuses on management and software development for the Tallobrix CRM platform (www.tallobrix.example)<br/><br/>I have a logo already designed...see attached.
Updates

Also Include my Name and Title: Marek T.L. Olvani President

Target Market(s)

Tallobrix Customers

Contact Information for Business Card

Only include my LOGO (provided)
My Name: Marek TL Olvani
My Title: President
My Company Name: Marek Olvani Consulting Inc.
My Website: www.marekolvaniconsulting.example
My Email: marek.olvani.consulting@mailbox.example

NO PHONE NUMBER
NO ADDRESS

Font styles to use
Serif
Sans Serif
Other font styles liked:
• see my website: www.marekolvaniconsulting.example

Colors

Designer to choose colors to be used in the design.

Requirements
Must have
• Must include my Orange
• Include my name (Marek T.L. Olvani), title (President) company name, website and email
• It should also have a tag line like: Tallobrix Consulting
• I'm flexible with the tag line
Should not have
• Don't include my phone number or address

```html
<!DOCTYPE html>
<html lang="en">
<head>
<meta charset="utf-8">
<title>Marek Olvani Consulting Inc. — Business Card</title>
<link rel="stylesheet" href="https://fonts.googleapis.com/css2?family=Exo+2:wght@400;500&family=Montserrat:wght@400;500&display=swap">
<style>
  :root {
    --orange: #f1811f;
    --ink: #3a3a3c;
    --card-dark: #1f2023;
    --map-tone: #2a2b2f;
    --paper: #ffffff;
    --backdrop: #dcdcdc;
    --light-text: #f4f4f4;
  }
  * { margin: 0; padding: 0; box-sizing: border-box; }
  html, body {
    width: 1173px;
    height: 1200px;
    overflow: hidden;
    background: var(--backdrop);
  }
  .card {
    position: absolute;
    width: 744px;
    height: 412px;
  }
  .card-front {
    left: 205px;
    top: 150px;
    background: var(--paper);
  }
  .card-back {
    left: 204px;
    top: 637px;
    background: var(--card-dark);
    overflow: hidden;
  }
  .holder-name {
    position: absolute;
    left: 68px;
    top: 66px;
    font-family: "Exo 2", sans-serif;
    font-weight: 500;
    font-size: 43px;
    line-height: 1;
    color: var(--orange);
    letter-spacing: 0.5px;
  }
  .holder-title {
    position: absolute;
    left: 68px;
    top: 110px;
    font-family: "Exo 2", sans-serif;
    font-weight: 500;
    font-size: 36px;
    line-height: 1;
    color: var(--ink);
  }
  .accent-rule {
    position: absolute;
    left: 67px;
    top: 163px;
    width: 49px;
    height: 6px;
    background: var(--orange);
  }
  .contact-list {
    position: absolute;
    left: 68px;
    top: 294px;
    list-style: none;
    font-family: "Montserrat", sans-serif;
    font-weight: 500;
    font-size: 19.5px;
    color: var(--ink);
  }
  .contact-list li {
    display: flex;
    align-items: center;
    gap: 7px;
    height: 29px;
  }
  .contact-list svg { width: 18px; height: 18px; flex: none; }
  .world-map {
    position: absolute;
    left: 6px;
    top: 46px;
    width: 734px;
    height: 342px;
    background: radial-gradient(ellipse at 55% 45%, var(--map-tone) 0%, var(--card-dark) 75%);
  }
  .brand-mark {
    position: absolute;
    left: 332px;
    top: 136px;
    width: 80px;
    height: 80px;
    background: var(--orange);
  }
  .company-name {
    position: absolute;
    left: 0;
    right: 0;
    top: 226px;
    text-align: center;
    font-family: "Exo 2", sans-serif;
    font-weight: 400;
    font-size: 31px;
    line-height: 1;
    color: var(--light-text);
  }
  .tagline {
    position: absolute;
    left: 0;
    right: 0;
    top: 262px;
    text-align: center;
    font-family: "Exo 2", sans-serif;
    font-weight: 400;
    font-size: 13px;
    letter-spacing: 1.6px;
    color: var(--light-text);
  }
</style>
</head>
<body>
  <section class="card card-front">
    <h1 class="holder-name">Marek TL Olvani</h1>
    <p class="holder-title">President</p>
    <div class="accent-rule"></div>
    <ul class="contact-list">
      <li>
        <svg viewBox="0 0 18 18" aria-hidden="true"><rect x="1" y="4" width="16" height="11" fill="var(--orange)"/><path d="M1 4 L9 10 L17 4 M1 15 L7 9 M17 15 L11 9" stroke="#fff" stroke-width="1.3" fill="none"/></svg>
        marek.olvani.consulting@mailbox.example
      </li>
      <li>
        <svg viewBox="0 0 18 18" aria-hidden="true"><circle cx="9" cy="9" r="8" fill="var(--orange)"/><path d="M4 6 Q7 5 8 8 Q7 11 9 13 M11 3 Q10 6 13 8 Q15 9 14 12" stroke="#fff" stroke-width="1.4" fill="none"/></svg>
        www.marekolvaniconsulting.example
      </li>
    </ul>
  </section>

  <section class="card card-back">
    <div class="world-map" role="img" aria-label="Faint dotted world map in the background"></div>
    <div class="brand-mark"></div>
    <h2 class="company-name">Marek Olvani Consulting Inc.</h2>
    <p class="tagline">Providing a full range of Tallobrix Consulting Services</p>
  </section>
</body>
</html>
```